Interactive Children's Media Book Company Website Design

We need a website DESIGN (no coding required) for a new interactive children's media book company called Tovira Studios.

We develop high-quality interactive children's books for the Lumo Tab/Lumo Phone that seeks to delight and inspire young and old alike. Our stories are filled with heart and spirit, and we seek to breathe magic back into books so that people fall back in love with reading.

Tovira means "butterfly" in Korean. It plays on the idea that a caterpillar metamorphoses into a butterfly - and in the same way, our readers are transformed through the journey of experiencing our interactive books.

We're looking for something based on the ATTACHED LOGO DESIGN for our company. A website that's professional, modern, fun and inviting; easy to read and not-cluttered, but still portraying the feeling of innocence and childhood.

We're looking for something that resonates the magical experience we want to create for our readers. Specific requirements on pages, tabs, content, etc are below.

• There are 7 tabs on the Homepage of the website: HOME, OUR GRANDPA, ABOUT US, CAREERS, NEWS, CONTACT US, SHOP. (But there is an extra page called YOUR GRANDPA, which will be a sub-page under Our Grandpa).

HOME
• Would be great to have some key images of our book (3-4 screen shots) as the key focus of the homepage that automatically scroll through every few seconds. (Placeholder image attached). The images would link to the “Our Grandpa” page.
• Company logo (attached to brief) and slogan: “A new era of children’s media” quite prominent on page.
• Key text content to be on page: “Tovira means “butterfly” in Korean. Just as a caterpillar transforms into a butterfly, Tovira Studios takes the reader on an unforgettable journey of metamorphosis through our stories. We turn children’s books into a high-quality interactive experience on mobile platforms - breathing magic back into books, and inspiring people to fall back in love with reading. Through our unique characters full of heart and spirit, our stories delight and inspire young and old alike.”
• Twitter & Facebook Like & Facebook page link icons.
• Section on Latest News with a few of the latest entries.
• Section on latest sister images & comments that visitors have posted, which takes you to the “Your Grandpa” page.

OUR GRANDPA
• The title for this page is “Our Grandpa Hums at Breakfast Time”
• There will be a little Lumo Tab/Lumo Phone icon (placeholder attached) for this book.
• There will be a link to the App Store to buy the app book.
• Key text content on this page: “Our debut interactive media book is coming soon on the Lumo Tab and Lumo Phone! “Our Grandpa Hums at Breakfast Time” touches on the beautiful and inextricable (albeit sometimes frustrating!) bond between sisters.”
• There will be a section on “Features” which lists all the various special features the app book includes.
• There will be a YouTube clip embedded into the page, which shows how the app book works.
• A section that says: “Do you have a sister who’s not like other sisters? Share a photo and tell us about her!” which links to the sub-page “Your Grandpa”.
• Under this, there may be the most recent few images submitted by the public, which when clicked on, would also link to the sub-page “Your Grandpa”.

YOUR GRANDPA
• The main text on the page: “Do you have a sister who’s not like other sisters? Share a photo and tell us about her!”
• Main body of the page is a gallery of all the photos that have been submitted. If you click on each of the images, you get the comments that people have submitted with the photos.
• The page would also have a Submit Comments Form, where people can upload a picture of their sister(s) and write a comment to accompany the image.

ABOUT US
• Introductory text on page: “It was a chance conversation at Harbourline Terminal, where two friends discovered they shared a dream to create quality children's media. Both of them were excited by the possibilities of using new digital platforms to inspire and educate a younger generation. From that idea Tovira Studios was born. We seek to be the chrysalis of story telling - to inspire the hearts and minds of our generation, and generations to come.”
• Section to “Join the Mailing List” where they can put their email address in and submit.
• Bios of 2x people with photos (bios in word doc attached) (do not have photos yet).

CAREERS
• The main text on the page: “We are always on the lookout for talented people to join our team. If you are a writer, illustrator, animator, iOS/android developer, musician, creative-writing translator - or have something special to offer Tovira Studios - we are keen to hear from you. Send us a message through the Contact Us tab above.”

NEWS
• Regular News page, with blog-type entries.

CONTACT US
• Online submit Contact Us form
• The main text on page: “Our studio is based in the Ember Craft Cooperative, 43 Pukeora Street, Marangai, Wellington. Ember is a professional, creative collective - with four separate studios, gallery, and retail store. For more information on Ember, visit: http://www.embercraftco.example.nz”
• “We would love to hear from you! Whether you have questions, ideas, comments, or just want to say hullo - please leave us a message and we will get back to you soon.”
• Including image of the premises (Ember image attached to brief).

SHOP
• Where visitors can purchase merchandise (t-shirts, mugs, etc) of the book/company.

```html
<!DOCTYPE html>
<html lang="en">
<head>
<meta charset="utf-8">
<title>Tovira Studios</title>
<link rel="stylesheet" href="https://fonts.googleapis.com/css2?family=Gochi+Hand&family=Mystery+Quest&family=Roboto:ital,wght@0,400;0,700;1,400&display=swap">
<style>
:root{
  --purple-deep:#6a43b8;
  --purple:#8a5fd6;
  --purple-tab:#7d4fd0;
  --purple-box:#6049a8;
  --lavender:#c9bdea;
  --lavender-soft:#e4dcf4;
  --sky:#1a9ad0;
  --sky-light:#2fc4ea;
  --ink:#4a4a4a;
  --grey-logo:#8c8c94;
  --white:#ffffff;
  --link:#1c8bc9;
  --foot:#5c3ea8;
}
*{box-sizing:border-box;margin:0;padding:0}
html,body{width:960px;height:1200px;overflow:hidden}
body{font-family:"Roboto",Arial,sans-serif;color:var(--ink);position:relative;
  background:linear-gradient(180deg,var(--purple-deep) 0,var(--purple) 300px,#9b7fd8 384px,var(--lavender) 385px,#b9aae2 448px,#bcaee4 449px,#d9d0f0 700px,#f6f3fc 880px,#ffffff 1040px,#ebe6f6 1086px,#f3f0fa 1087px,#e2dbf2 1150px,#8a6fd0 1151px,#6d4fc0 1200px);}
.glow{position:absolute;left:300px;top:-120px;width:420px;height:420px;border-radius:50%;
  background:radial-gradient(circle,rgba(255,255,255,.95) 0,rgba(255,255,255,.55) 35%,rgba(255,255,255,0) 70%)}
.glow.logo-glow{left:20px;top:-60px;width:260px;height:220px}
.abs{position:absolute}
/* logo */
.brand{left:76px;top:40px;display:flex;align-items:center;gap:12px}
.brand-dot{width:48px;height:48px;border-radius:50%;background:var(--purple)}
.brand-name{font-size:34px;font-weight:400;color:var(--grey-logo);letter-spacing:1px}
/* nav */
.nav{left:308px;top:98px;display:flex;gap:5px}
.nav a{display:block;width:83px;height:34px;border-radius:4px 4px 0 0;background:linear-gradient(180deg,#9a6ee6,var(--purple-tab));
  color:var(--white);font-family:"Gochi Hand",cursive;font-size:16px;text-align:center;line-height:32px;text-decoration:none;border:1px solid #b99cf0;border-bottom:none}
/* hero */
.hero-frame{left:70px;top:120px;width:820px;height:324px;background:var(--white);border-radius:6px;box-shadow:0 2px 6px rgba(60,30,120,.35)}
.hero-card{left:80px;top:130px;width:800px;height:302px;background:var(--white);border-radius:8px;box-shadow:0 1px 4px rgba(0,0,0,.2)}
.hero-scene{left:96px;top:156px;width:765px;height:246px;overflow:hidden;border-radius:0 40px 0 0;
  background:linear-gradient(90deg,#4f8a3a 0,#c59a5a 32%,#3a8ccf 52%,#1aa6de 75%,var(--sky-light) 100%)}
.slogan{left:548px;top:212px;width:260px;text-align:center;font-family:"Mystery Quest",cursive;color:var(--white);font-size:38px;line-height:52px}
.dots{left:108px;top:375px;display:flex;gap:6px}
.dots span{width:18px;height:18px;border-radius:50%;border:2px solid var(--white);background:rgba(255,255,255,.2)}
.dots span:first-child{background:rgba(255,255,255,.6)}
.cta{left:460px;top:381px;width:252px;height:40px;border-radius:4px;background:linear-gradient(180deg,#a57ff0,#8656d8);
  color:var(--white);font-weight:700;font-size:14px;text-align:center;line-height:40px;box-shadow:0 2px 4px rgba(0,0,0,.25)}
.device{border-radius:6px;background:linear-gradient(160deg,#2a2a2a,#000);padding:5px}
.device div{width:100%;height:100%;border-radius:2px;background:radial-gradient(circle at 55% 40%,#e6b3ef,#9b4fb7 40%,#1e0e2a 80%)}
.device.tab{left:778px;top:324px;width:91px;height:118px}
.device.phone{left:731px;top:370px;width:41px;height:74px;border-radius:7px;padding:4px 3px 12px}
.social{left:40px;top:310px;display:flex;flex-direction:column;gap:4px}
.social span{width:38px;height:36px;border-radius:4px;background:linear-gradient(180deg,#4fb5ef,#1c7fc4);border:2px solid #bde3fb}
/* welcome */
.card{background:var(--white);border-radius:4px;box-shadow:0 1px 4px rgba(60,30,120,.3)}
.welcome{left:80px;top:472px;width:333px;height:237px;padding:14px 13px}
.h2{font-size:22px;font-weight:400;color:var(--sky)}
.welcome p{margin-top:16px;font-size:11.5px;line-height:14px;color:#555}
.welcome .quote{margin-top:10px;text-align:center;font-size:14.5px;color:var(--sky)}
.thumb{width:147px;height:114px;padding:6px}
.thumb div{width:100%;height:100%}
/* news */
.news{left:93px;top:730px;width:310px}
.news p,.comments p{margin-top:10px;font-size:11.5px;line-height:14px;color:#555}
.divider{left:418px;top:730px;width:1px;height:146px;background:#cfc5ea}
.comments{left:437px;top:730px;width:430px}
.comments p{margin-top:10px}
.comments p+p{margin-top:12px}
.comments b{color:var(--link)}
a.more,.by{color:var(--link);font-style:italic;text-decoration:none}
/* carousel */
.slot{top:917px;width:147px;height:114px;padding:6px}
.slot div{width:100%;height:100%;border-radius:3px;background:var(--purple-box)}
.arrow{top:954px;width:36px;height:36px;border-radius:50%;background:radial-gradient(circle at 50% 35%,#fff,#ddd3f2);box-shadow:0 1px 3px rgba(0,0,0,.35)}
.arrow svg{display:block}
/* footer */
.footer{left:80px;top:1110px;width:800px;display:flex;justify-content:space-between;font-size:12px;color:var(--foot)}
.footer a{color:var(--foot);text-decoration:none}
</style>
</head>
<body>
<div class="glow"></div>
<div class="glow logo-glow"></div>

<div class="abs brand"><span class="brand-dot"></span><span class="brand-name">Tovira Studios</span></div>

<nav class="abs nav">
  <a href="#">Home</a><a href="#">About Us</a><a href="#">Our Grandpa</a><a href="#">Shop</a><a href="#">Careers</a><a href="#">Contact Us</a>
</nav>

<div class="abs hero-frame"></div>
<div class="abs hero-card"></div>
<div class="abs hero-scene" role="img" aria-label="Book illustration: a smiling girl in a backyard beside a wooden fence and house, under a blue sky"></div>
<div class="abs slogan">A new era of<br>children’s media</div>
<div class="abs dots"><span></span><span></span><span></span><span></span></div>
<div class="abs cta">Available on Lumo Phone &amp; Lumo Tab</div>
<div class="abs device phone" role="img" aria-label="Phone showing the book app"><div></div></div>
<div class="abs device tab" role="img" aria-label="Tablet showing the book app"><div></div></div>
<div class="abs social" aria-label="Social links"><span role="img" aria-label="Social page link"></span><span role="img" aria-label="Social feed link"></span></div>

<section class="abs card welcome">
  <h2 class="h2">Welcome to Tovira</h2>
  <p><b>“Tovira means “butterfly”</b> in Korean. Just as a caterpillar transforms into a butterfly, Tovira Studios takes the reader on an unforgettable journey of metamorphosis through our stories. We turn children’s books into a high-quality interactive experience on mobile platforms - breathing magic back into books, and inspiring people to fall back in love with reading. Through our unique characters full of heart and spirit, our stories delight and inspire young and old alike.</p>
  <p class="quote">“Breathing magic back into books”</p>
</section>

<div class="abs card thumb" style="left:424px;top:472px"><div role="img" aria-label="Illustration: a smiling sun" style="background:linear-gradient(135deg,#ffe23a,#f5a623 60%,#5ab3e6)"></div></div>
<div class="abs card thumb" style="left:579px;top:472px"><div role="img" aria-label="Illustration: blue house rooftops" style="background:linear-gradient(160deg,#7cc8ee,#3a63b8)"></div></div>
<div class="abs card thumb" style="left:734px;top:472px"><div role="img" aria-label="Illustration: tree branch with leaves" style="background:linear-gradient(135deg,#2f6a2a,#7a4a2a)"></div></div>
<div class="abs card thumb" style="left:424px;top:595px"><div role="img" aria-label="Illustration: the girl character smiling" style="background:linear-gradient(135deg,#e37a3a,#f2c7a8 55%,#b08a5a)"></div></div>
<div class="abs card thumb" style="left:579px;top:595px"><div role="img" aria-label="Illustration: a red-roofed doghouse" style="background:linear-gradient(160deg,#8fbf3a,#c53a2a 45%,#e8d67a)"></div></div>
<div class="abs card thumb" style="left:734px;top:595px"><div role="img" aria-label="Illustration: wooden fence and tree" style="background:linear-gradient(180deg,#5fa7dd,#3f8a3a 35%,#c28a4a)"></div></div>

<section class="abs news">
  <h2 class="h2">Latest News</h2>
  <p>Lorem ipsum dolor sit amet, consectetur adipiscing elit. Fusce ut turpis tellus. Nulla eu elit quam. Vivamus convallis tincidunt nibh quis auctor. Aliquam in sem nisl, interdum aliquet felis. Class aptent taciti sociosqu ad litora torquent per conubia nostra, per inceptos himenaeos. Curabitur nunc leo, molestie vitae sollicitudin a, eleifend sit amet tortor. Phasellus <a class="more" href="#">More...</a></p>
</section>
<div class="abs divider"></div>
<section class="abs comments">
  <h2 class="h2">Comments</h2>
  <p><b>Lorem ipsum dolor sit amet</b>, consectetur adipiscing elit. Fusce ut turpis tellus. Nulla eu elit quam. Vivamus convallis tincidunt nibh quis auctor. Aliquam in sem nisl. <span class="by">By Lorum Ipsum</span></p>
  <p><b>Interdum aliquet felis.</b> Class aptent taciti sociosqu ad litora torquent per conubia nostra, per inceptos himenaeos. Curabitur nunc leo, molestie vitae sollicitudin a, eleifend sit amet tortor. Phasellus egestas nulla eget nulla vestibulum sollicitudin. <span class="by">By Lorum Ipsum</span></p>
</section>

<div class="abs arrow" style="left:94px"><svg width="36" height="36" viewBox="0 0 36 36"><path d="M8 18 L17 10 V15 H27 V21 H17 V26 Z" fill="#5a3aa8"/></svg></div>
<div class="abs card slot" style="left:142px"><div></div></div>
<div class="abs card slot" style="left:318px"><div></div></div>
<div class="abs card slot" style="left:494px"><div></div></div>
<div class="abs card slot" style="left:669px"><div></div></div>
<div class="abs arrow" style="left:828px"><svg width="36" height="36" viewBox="0 0 36 36"><path d="M28 18 L19 10 V15 H9 V21 H19 V26 Z" fill="#5a3aa8"/></svg></div>

<footer class="abs footer">
  <span>© Copyright 2011 Tovira Studios</span>
  <span><a href="#">Privacy</a> I <a href="#">Sitemap</a> I <a href="#">Contact</a></span>
</footer>
</body>
</html>
```